Moving offices: new address and other details notification postcard

We are a small firm of accountants moving offices for the first time in 30 years. The project is to produce a postcard that we can send to customers, suppliers and other business contacts letting them know that we are moving and advising our new address.. Attached is our logo and also a sketch we found through google of Tarrow Vale Parade in London which is where we are moving to and we thought might be a suitable as part of the card. Ideally we want something that will communicate our new contact details and from which people will update there systems rather than simply just file the card in the bin!
I understand that the card may need to be mailed in an envelope to stop Crestline Post returning it like a boomerang.
Our website is
www.quellinandco.biz

```html
<!DOCTYPE html>
<html lang="en">
<head>
<meta charset="utf-8">
<title>Quellin &amp; Co. – We are moving</title>
<link href="https://fonts.googleapis.com/css2?family=Lato:wght@400;700&display=swap" rel="stylesheet">
<style>
  :root {
    --brand-red: #c8102e;
    --ink: #2b2b2b;
    --band-dark: #1f56a8;
    --band-light: #a9c6ea;
    --panel-blue: #a7cbec;
    --panel-grey: #e3e3e3;
    --card-bg: #ffffff;
    --page-bg: #ffffff;
    --sky-top: #f3eef2;
    --sky-pink: #e6c3d3;
    --street-dark: #4a3a34;
    --street-warm: #b07a55;
  }
  * { box-sizing: border-box; margin: 0; padding: 0; }
  html, body {
    width: 835px; height: 1200px; overflow: hidden;
    background: var(--page-bg);
    font-family: "Lato", "Gill Sans", sans-serif;
    color: var(--ink);
  }
  .canvas { position: relative; width: 835px; height: 1200px; }

  .card {
    position: absolute; left: 76px; width: 656px;
    background: var(--card-bg);
    box-shadow: 4px 6px 10px rgba(0,0,0,0.25);
    overflow: hidden;
  }

  /* Front */
  .card--front { top: 14px; height: 570px; }
  .street-scene {
    position: absolute; inset: 0;
    background:
      linear-gradient(180deg, transparent 55%, rgba(74,58,52,0.55) 100%),
      linear-gradient(90deg, var(--street-dark) 0%, rgba(74,58,52,0.6) 22%, transparent 40%, transparent 62%, rgba(176,122,85,0.6) 78%, var(--street-dark) 100%),
      linear-gradient(180deg, var(--sky-top) 0%, var(--sky-pink) 45%, var(--street-warm) 100%);
  }
  .front-brand {
    position: absolute; top: 22px; right: 26px;
    display: flex; align-items: center; gap: 12px;
  }
  .brand-dot {
    width: 54px; height: 54px; border-radius: 50%;
    background: var(--brand-red);
  }
  .front-brand__text { font-size: 22px; line-height: 1.25; color: var(--ink); }

  /* Back */
  .card--back { top: 617px; height: 500px; }
  .back-band {
    position: absolute; left: 0; top: 0; width: 502px; height: 131px;
    background: linear-gradient(200deg, var(--band-light) 0%, var(--band-dark) 70%);
    display: flex; align-items: center; gap: 18px; padding-left: 30px;
  }
  .brand-dot--light { background: var(--card-bg); width: 84px; height: 84px; }
  .back-band__text { color: #fff; font-size: 36px; line-height: 1.3; }
  .address-panel {
    position: absolute; left: 0; top: 131px; width: 314px; height: 314px;
    background: var(--panel-blue);
    padding: 20px 18px 0 16px;
  }
  .address-line { height: 1.5px; background: #ffffff; margin-bottom: 28px; }
  .contact-panel {
    position: absolute; left: 314px; top: 150px; width: 342px; height: 272px;
    background: var(--panel-grey);
    padding: 12px 0 0 20px;
    font-size: 22px; line-height: 1.33;
  }
  .contact-panel__title { color: var(--brand-red); font-size: 20px; margin-bottom: 10px; }
  .contact-panel__address { padding-left: 50px; margin-bottom: 12px; }
  .contact-row { font-size: 19px; }
  .contact-row__label { color: var(--brand-red); display: inline-block; width: 58px; }
</style>
</head>
<body>
<div class="canvas">
  <section class="card card--front">
    <div class="street-scene" role="img" aria-label="Sketch of Tarrow Vale Parade in London at dusk: terraced shops, a church spire and a pink evening sky"></div>
    <div class="front-brand">
      <span class="brand-dot"></span>
      <p class="front-brand__text">Quellin &amp; Co.<br>Established 1962</p>
    </div>
  </section>

  <section class="card card--back">
    <header class="back-band">
      <span class="brand-dot brand-dot--light"></span>
      <p class="back-band__text">Quellin &amp; Co.<br>Established 1962</p>
    </header>
    <div class="address-panel" aria-label="Recipient address lines">
      <div class="address-line"></div><div class="address-line"></div>
      <div class="address-line"></div><div class="address-line"></div>
      <div class="address-line"></div><div class="address-line"></div>
      <div class="address-line"></div><div class="address-line"></div>
      <div class="address-line"></div>
    </div>
    <div class="contact-panel">
      <p class="contact-panel__title">Contact Us Today</p>
      <address class="contact-panel__address" style="font-style:normal">
        Quellin &amp; Co.<br>Marlow Grant House,<br>318 Tarrow Road,<br>London,<br>N27 4KX
      </address>
      <p class="contact-row"><span class="contact-row__label">E-mail:</span>enquiries@quellinandco.biz</p>
      <p class="contact-row"><span class="contact-row__label">Tel:</span>(0)20 7946 0182</p>
    </div>
  </section>
</div>
</body>
</html>
```